Online Marketing Website

Create a website design for an online marketing company.

It should use modern designs:

Power of space,
Graphics supported content - less words more meaning
Grid and flow layout for listing type content
Provision for responsive and interactive CSS

http://www.brightkettlemedia.com.au/ is a very quick mock up, however this should only be used as an example and is not a indication of desired design. Examples that differ from this will be considered.
Updates

To all the developers who have submitted a design, There are a lot a great designs there. I am going to wait a little while longer before providing any feedback as I do not like wasting your time, and experience has shown good designs come late.

At this stage no news is not bad news... It is just that.

Thanks heaps for your work, will contact the leaders soon.

Target Market(s)

Small to Medium Business operating in the B2B or professional B2C space

Industry/Entity Type

Marketing

Requirements
Must have
• It should use a modern Panel design for the front page that will give a high level overview of the products with in-depth content pages for each service.

Nice to have
• Rotating banner at the top of the pages, no higher than 300px

Appropriate use of power colours such as red and Orange.
Should not have
• No Sidebars except on Post pages

```html
<!DOCTYPE html>
<html lang="en">
<head>
<meta charset="utf-8">
<title>Bright Kettle Media</title>
<link rel="stylesheet" href="https://fonts.googleapis.com/css2?family=Yanone+Kaffeesatz:wght@300;400&family=Roboto:wght@300;400&display=swap">
<style>
  :root{
    --ink-dark:#2f3038;
    --hero-red:#e8442f;
    --hero-orange:#ee5a2c;
    --orange:#f07f13;
    --amber:#f5a000;
    --crimson:#d7193f;
    --grey-text:#6b6b6b;
    --title-text:#3a3a3a;
    --panel-light:#f4f4f5;
    --tile-grey:#e4e4e4;
    --green:#b4c11a;
    --tile-orange:#f0641e;
    --tile-red:#e5183f;
    --tile-blue:#49aee8;
    --white:#ffffff;
  }
  *{box-sizing:border-box;margin:0;padding:0}
  html,body{width:734px;height:1200px;overflow:hidden}
  body{position:relative;background:var(--white);font-family:"Yanone Kaffeesatz",sans-serif;font-weight:300;color:var(--grey-text)}
  .abs{position:absolute}

  /* header */
  .site-header{position:absolute;left:0;top:0;width:734px;height:52px;background:var(--ink-dark)}
  .brand{position:absolute;left:94px;top:14px;display:flex;align-items:center;gap:7px}
  .brand-mark{width:18px;height:18px;background:var(--amber);border-radius:2px}
  .brand-name{font-family:"Roboto",sans-serif;font-weight:400;font-size:16px;color:var(--white);letter-spacing:.2px}
  .social{position:absolute;left:483px;top:22px;display:flex;gap:5px}
  .social span{width:14px;height:14px;background:#45464e;border-radius:2px;display:block}
  .social span.active{background:var(--amber)}
  .social .search{display:flex;align-items:center;justify-content:center}
  .menu-btn{position:absolute;left:628px;top:21px;width:16px;height:16px;border:1px solid #45464e;border-radius:2px;display:flex;flex-direction:column;justify-content:center;gap:2px;padding:0 4px}
  .menu-btn i{display:block;height:1.5px;background:var(--crimson)}

  /* hero */
  .hero{position:absolute;left:0;top:52px;width:734px;height:174px;background:linear-gradient(90deg,var(--hero-red),var(--hero-orange))}
  .hero-arrow{position:absolute;top:68px;width:30px;height:30px;background:rgba(255,255,255,.3);display:flex;align-items:center;justify-content:center}
  .hero-title{position:absolute;left:133px;top:25px;font-size:29px;font-weight:400;color:var(--white)}
  .hero-text{position:absolute;left:134px;top:60px;width:262px;font-size:14px;line-height:17.5px;color:#ffe1d6}
  .hero-btn{position:absolute;left:133px;top:122px;width:78px;height:26px;background:var(--white);border-radius:2px;color:var(--hero-red);font-size:13px;display:flex;align-items:center;justify-content:center}
  .hero-graphic{position:absolute;left:434px;top:76px;width:172px;height:170px;border-radius:50%;background:conic-gradient(#b9cc2a 0 25%,#f08a2a 25% 40%,#c0186a 40% 55%,#7d27b0 55% 70%,#3b9fe0 70% 90%,transparent 90%);opacity:.95}

  /* customers */
  .section-title{position:absolute;left:0;width:734px;text-align:center;font-weight:300}
  .customers-title{top:258px;font-size:39px;color:var(--title-text)}
  .customers-sub{top:301px;font-size:15px;color:var(--amber)}
  .customers-text{position:absolute;left:104px;top:326px;width:526px;text-align:center;font-size:12px;line-height:14px}
  .stat{position:absolute;top:380px;width:120px;text-align:center}
  .stat-tile{position:relative;width:82px;height:82px;margin:0 auto;border-radius:8px;background:var(--tile-grey);overflow:hidden}
  .stat-fill{position:absolute;right:0;top:0}
  .stat-face{position:absolute;left:8px;top:8px;width:66px;height:66px;background:var(--white);border-radius:3px;display:flex;align-items:center;justify-content:center;font-family:"Roboto",sans-serif;font-weight:300;font-size:25px}
  .stat-face small{font-size:17px;margin-top:4px}
  .stat-label{margin-top:7px;font-size:15px;color:var(--title-text)}
  .stat-note{margin-top:4px;font-size:10.5px;line-height:12.5px}

  /* metrics */
  .metrics{position:absolute;left:0;top:566px;width:734px;height:175px;background:var(--panel-light);border-top:1px solid #e8e8e8}
  .metrics-title{top:24px;font-size:38px;color:var(--crimson)}
  .metrics-text{position:absolute;left:0;top:79px;width:734px;text-align:center;font-size:11.5px;line-height:13.5px}
  .metrics-btn{position:absolute;left:330px;top:126px;width:77px;height:27px;background:var(--crimson);color:var(--white);font-size:13px;display:flex;align-items:center;justify-content:center;border-radius:1px}

  /* content */
  .content{position:absolute;left:0;top:741px;width:734px;height:339px;background:var(--orange)}
  .content-title{top:35px;font-size:37px;color:var(--white)}
  .content-copy{position:absolute;left:101px;top:99px;width:248px;font-size:11px;line-height:13.6px;color:var(--white)}
  .content-copy p{margin-bottom:13.6px}
  .browser{position:absolute;left:371px;top:97px;width:274px;height:242px;background:#fb9700}
  .browser-bar{height:22px;background:#e2e2e2;display:flex;align-items:center;gap:3px;padding-left:7px}
  .browser-bar i{width:6px;height:6px;border-radius:50%;background:#b4b4b4;display:block}

  /* plan */
  .plan{position:absolute;left:0;top:1080px;width:734px;height:120px;background:var(--ink-dark)}
  .plan-title{top:40px;font-size:37px;color:var(--amber)}
</style>
</head>
<body>

<header class="site-header">
  <div class="brand"><span class="brand-mark"></span><span class="brand-name">BRIGHT KETTLE MEDIA</span></div>
  <nav class="social" aria-label="Social links">
    <span class="active"></span><span></span><span></span><span></span><span></span>
    <span class="search"><svg width="9" height="9" viewBox="0 0 10 10"><circle cx="4" cy="4" r="3" fill="none" stroke="#9a9aa2" stroke-width="1.4"/><path d="M6.3 6.3 9 9" stroke="#9a9aa2" stroke-width="1.4"/></svg></span>
  </nav>
  <div class="menu-btn"><i></i><i></i><i></i></div>
</header>

<section class="hero">
  <div class="hero-arrow" style="left:19px"><svg width="10" height="14" viewBox="0 0 10 14"><path d="M8 1 2 7l6 6" fill="none" stroke="#fff" stroke-width="1.6"/></svg></div>
  <div class="hero-arrow" style="left:685px"><svg width="10" height="14" viewBox="0 0 10 14"><path d="M2 1l6 6-6 6" fill="none" stroke="#fff" stroke-width="1.6"/></svg></div>
  <h1 class="hero-title">Online Strategic Planning?</h1>
  <p class="hero-text">An Online Strategic Plan is a lot like a business plan. You define look at your business, define your values, look at your competitors...</p>
  <a class="hero-btn">Learn More...</a>
</section>
<div class="hero-graphic" role="img" aria-label="Circular planning cycle graphic: website, evaluation, goals, actions, measure, improve"></div>

<h2 class="section-title customers-title">Identify Your Customers</h2>
<p class="section-title customers-sub">Do you really know your customers?</p>
<p class="customers-text">Who are they? What are they looking for when wanting your service? What are their preferences in browsing device? What is making them leave your pages before they have read the content you want them to?</p>

<div class="stat" style="left:123px">
  <div class="stat-tile" style="background:linear-gradient(135deg,#c9d22a,#a3a616)"><div class="stat-face" style="color:#a9b31a">90<small>%</small></div></div>
  <div class="stat-label">Leave before 6s</div>
  <div class="stat-note">Unless finding what they want, 90% of visitors will click off your page within 6 seconds!</div>
</div>
<div class="stat" style="left:245px">
  <div class="stat-tile"><div class="stat-fill" style="width:26px;height:78px;background:var(--tile-orange);border-top-right-radius:8px"></div><div class="stat-face" style="color:var(--tile-orange)">33<small>%</small></div></div>
  <div class="stat-label">Searchly Users</div>
  <div class="stat-note">33% use Searchly+</div>
</div>
<div class="stat" style="left:370px">
  <div class="stat-tile"><div class="stat-fill" style="width:41px;height:68px;background:var(--tile-red);border-top-right-radius:8px"></div><div class="stat-face" style="color:var(--tile-red)">41<small>%</small></div></div>
  <div class="stat-label">Friendbook Users</div>
  <div class="stat-note">41% prefer Friendbook</div>
</div>
<div class="stat" style="left:489px">
  <div class="stat-tile"><div class="stat-fill" style="width:30px;height:33px;background:var(--tile-blue);border-top-right-radius:8px"></div><div class="stat-face" style="color:var(--tile-blue)">31<small>%</small></div></div>
  <div class="stat-label">Tablet Users</div>
  <div class="stat-note">31% of all users are using<br>a tablet device</div>
</div>

<section class="metrics">
  <h2 class="section-title metrics-title">Do you know your metrics?</h2>
  <p class="metrics-text">Do you know what content is converting your visitors or worse, which content is driving them away!<br>We work with you to develop strategies to identify this information, that allows you to optimise your content for your visitor’s preferences.</p>
  <a class="metrics-btn">Learn More...</a>
</section>

<section class="content">
  <h2 class="section-title content-title">Create content that sells</h2>
  <div class="content-copy">
    <p>We work with you, provide the tools and support that will allow you to create content on a regular basis that will sell you business to your customers.</p>
    <p>The key to SEO in 2014 and beyond is CONTENT. Great, regular updated content. This is great, no longer is SEO a black art of tricking the search engines into returning your content by faking a whole lot of backlinks. Now it is all about providing valuable content to your customers, decreasing customer bounce rates, and in return you get great search rankings.</p>
    <p>But we understand that the idea of producing at least an article, blog or landing page a week is dumbfounding, however can make it easy, and only take a few minutes a week of your time.</p>
    <p>Sounds like a win-win.</p>
  </div>
  <div class="browser"><div class="browser-bar"><i></i><i></i><i></i></div></div>
</section>

<section class="plan">
  <h2 class="section-title plan-title">Whats the plan?</h2>
</section>

</body>
</html>
```